Can you design the Future of Mealworm Pet Food Packaging for me?

Project Overview:
We are seeking a dynamic and visually striking product label design for our range of mealworm pet food supplements. The label must effectively showcase the product, accommodate various container and packaging sizes, and include essential information such as a barcode, ingredients list, company address, and instructions for use. The design should exude positivity, capture the attention of consumers, and convey the quality and value of the product.

Target Audience:
Our target audience consists of health-conscious pet owners, aged 25-55, who prioritize quality, sustainability, and aesthetic appeal in their purchasing decisions. They are drawn to visually appealing packaging that conveys trustworthiness and authenticity.

Key Objectives:

Create a visually impactful label design that stands out on shelves and online platforms.
Clearly showcase the product while leaving space for essential information.
Ensure versatility to fit various container and packaging sizes.
Convey positivity, quality, and authenticity to resonate with our target audience.
Facilitate ease of use and readability for consumers.

Design Requirements:

Product Showcase: The label should prominently feature the product, with high-quality imagery, words or illustrations that highlight its key attributes and appeal to the target audience.

Space for Essential Information:
The design must include designated areas for a barcode, ingredients list, company address, and instructions for use. These elements should be clearly legible and easily accessible to consumers.

Versatility: The label design should be adaptable to different container shapes and sizes, including bottles, jars, and pouches. It should maintain its visual impact and readability across various packaging formats.

Positive Visual Impact: Incorporate colors, fonts, and imagery that evoke feelings of positivity, vitality, and well-being. Avoid clutter and maintain a clean, modern aesthetic. An example from a competitor company is attached for information.

To help provide you some focus, the first labels to be used in our production will measure 14cm x 6cm and the contents will weigh 20g

Please contact me if you have any questions about this brief or would like more info to help with your design. Thank you and I look forward to seeing your design.

Target Market(s)

Target Audience: Our target audience consists of health-conscious pet owners, aged 25-55, who prioritize quality, sustainability, and aesthetic appeal in their purchasing decisions. They are drawn to visually appealing packaging that conveys trustworthiness and authenticity.

Industry/Entity Type

Pet Food

Requirements
Must have
• Key Objectives: Create a visually impactful label design that stands out on shelves and online platforms. Clearly showcase the product while leaving space for essential information. Ensure versatility to fit various container and packaging sizes. Convey positivity, quality, and authenticity to resonate with our target audience. Facilitate ease of use and readability for consumers.
Nice to have
• Maintain a clean, modern aesthetic
Should not have
• Avoid clutter

```html
<!DOCTYPE html>
<html lang="en">
<head>
<meta charset="UTF-8">
<title>Brindlebite Mealworm Supplement Label</title>
<link href="https://fonts.googleapis.com/css2?family=Playfair+Display:wght@600&family=Quicksand:wght@400;500;600&family=Dancing+Script:wght@500&display=swap" rel="stylesheet">
<style>
  :root {
    --rust: #a4441c;
    --rust-dark: #7c2f11;
    --rust-soft: #c9764a;
    --leaf: #1e7b32;
    --paper: #fbfaf8;
    --ink: #8a3a17;
    --stage: #c9d6dc;
  }
  * { box-sizing: border-box; margin: 0; padding: 0; }
  html, body { width: 1200px; height: 965px; overflow: hidden; }
  body {
    background: var(--stage);
    font-family: "Quicksand", sans-serif;
    color: var(--ink);
    position: relative;
  }
  .label {
    position: absolute;
    left: 30px; top: 238px;
    width: 1140px; height: 489px;
    background: var(--paper);
    overflow: hidden;
  }
  .panel { position: absolute; top: 0; bottom: 26px; }
  .panel--usage { left: 0; width: 400px; padding: 26px 28px 0 30px; }
  .panel--front { left: 400px; width: 380px; }
  .panel--info { left: 780px; width: 360px; }

  .tag {
    display: inline-block;
    background: var(--rust);
    color: var(--paper);
    font-weight: 600;
    font-size: 12px;
    padding: 3px 9px;
  }
  .usage-list { list-style: none; margin-top: 8px; font-size: 12.5px; line-height: 1.42; font-weight: 500; }
  .vet-bar {
    margin-top: 10px;
    background: var(--rust);
    color: var(--paper);
    font-weight: 600;
    font-size: 13px;
    padding: 4px 10px;
  }
  .storage-box {
    border: 1px solid var(--rust);
    font-size: 10.5px;
    padding: 5px 10px;
    margin-top: 4px;
  }
  .review { margin-top: 14px; }
  .review .tag { font-size: 10px; font-weight: 500; }
  .review-text {
    font-family: "Dancing Script", cursive;
    font-size: 13.5px;
    line-height: 1.38;
    margin-top: 6px;
  }
  .review-author { text-align: right; font-size: 11px; margin-top: 2px; }

  .bottom-band {
    position: absolute; left: 0; right: 0; bottom: 0; height: 26px;
    background: var(--rust);
    color: var(--paper);
    font-size: 12.5px; font-weight: 600; letter-spacing: .4px;
    padding: 5px 0 0 30px;
  }

  .organic-ribbon {
    position: absolute; left: 22px; top: 22px;
    width: 28px; height: 42px;
    background: var(--leaf);
    clip-path: polygon(0 0,100% 0,100% 100%,50% 80%,0 100%);
  }
  .brand-block {
    position: absolute; left: 100px; top: 0;
    width: 180px; height: 86px;
    background: var(--rust);
    clip-path: polygon(0 0,100% 0,100% 84%,0 100%);
    display: flex; align-items: center; justify-content: center; gap: 6px;
    color: var(--paper);
    font-weight: 600; font-size: 11.5px; letter-spacing: .5px;
    padding-bottom: 6px;
    white-space: nowrap;
  }
  .brand-block .dot { width: 8px; height: 8px; border-radius: 50%; background: var(--paper); flex: none; }
  .product-name {
    position: absolute; left: 0; right: 0; top: 92px;
    text-align: center;
    font-family: "Playfair Display", serif;
    font-weight: 600; font-size: 48px;
    color: var(--rust);
    letter-spacing: .5px;
  }
  .hero-photo {
    position: absolute; left: 96px; top: 160px;
    width: 190px; height: 190px;
  }
  .supports {
    position: absolute; left: 26px; top: 345px;
  }
  .supports .tag {
    background: linear-gradient(90deg,var(--rust),var(--rust-soft) 70%,transparent);
    font-size: 13px; font-weight: 500; padding: 2px 40px 2px 10px;
  }
  .supports ul { list-style: none; margin-top: 4px; font-size: 15px; font-weight: 500; line-height: 1.15; color: var(--rust-dark); }
  .supports li::before { content: "\25B8"; color: var(--rust); font-size: 10px; margin-right: 4px; }
  .net-weight { position: absolute; left: 300px; top: 330px; font-size: 15px; color: var(--rust); }
  .allergy {
    position: absolute; left: 210px; top: 420px;
    display: flex; align-items: center; gap: 6px;
    font-size: 14px; color: var(--rust-dark);
  }

  .about {
    position: absolute; left: 20px; right: 30px; top: 18px; height: 200px;
    background: var(--rust);
    color: var(--paper);
    font-size: 12px; line-height: 1.5;
    padding: 16px 20px;
  }
  .ingredients { position: absolute; left: 20px; right: 30px; top: 232px; }
  .ingredients .tag { font-size: 11px; font-weight: 500; }
  .ingredients p { font-size: 11.5px; line-height: 1.45; margin-top: 6px; }
  .contact { position: absolute; left: 20px; top: 334px; font-size: 10px; line-height: 1.55; }
  .contact strong { font-weight: 600; }
  .batch {
    position: absolute; left: 20px; right: 30px; top: 410px;
    border-top: 1px solid var(--rust);
    padding-top: 5px;
    font-size: 10px; line-height: 1.5;
  }
  .edge-strip { position: absolute; right: 0; top: 0; bottom: 0; width: 14px; background: var(--rust); }
</style>
</head>
<body>
  <main class="label">
    <section class="panel panel--usage">
      <span class="tag">Instructions for Use:</span>
      <ul class="usage-list">
        <li>Serve as a supplement to your pet's regular diet.</li>
        <li>Consult with your veterinarian for specific feeding recommendations.</li>
        <li>Daily serving size based on pet's size:</li>
        <li>Small pets: 1-2 teaspoons</li>
        <li>Medium pets: 1-2 tablespoons</li>
        <li>Large pets: 2-4 tablespoons</li>
        <li>Sprinkle on food or mix with water.</li>
        <li>Observe pet's intake and adjust serving size if needed.</li>
        <li>Monitor for any adverse reactions and discontinue use if necessary. Keep fresh water available at all times.</li>
      </ul>
      <div class="vet-bar">Consult veterinarian for concerns or questions.</div>
      <div class="storage-box">Store in a cool, dry place and seal tightly after each use.</div>
      <div class="review">
        <span class="tag">CUSTOMER REVIEW</span>
        <p class="review-text">A Must-Have for Pet Owners! My pup, Max, can't get enough of Quillory's mealworm supplement! It's made a noticeable difference in his energy and coat. Knowing it's packed with quality ingredients gives me peace of mind. Highly recommend!</p>
        <p class="review-author">Lena R.</p>
      </div>
    </section>

    <section class="panel panel--front">
      <div class="organic-ribbon" aria-hidden="true"></div>
      <div class="brand-block"><span class="dot"></span>FERNVALE NUTRITION</div>
      <h1 class="product-name">Brindlebite</h1>
      <svg class="hero-photo" viewBox="0 0 190 190" role="img" aria-label="Photo of a happy golden puppy beside a bowl of dried mealworms">
        <defs>
          <radialGradient id="heroFill" cx="50%" cy="45%" r="60%">
            <stop offset="0" stop-color="#f1dcbc"/>
            <stop offset="0.7" stop-color="#dcb487"/>
            <stop offset="1" stop-color="#f4efe8"/>
          </radialGradient>
        </defs>
        <circle cx="95" cy="95" r="92" fill="url(#heroFill)" stroke="var(--rust)" stroke-width="2"/>
      </svg>
      <span class="net-weight">20g e</span>
      <div class="supports">
        <span class="tag">SUPPORTS</span>
        <ul>
          <li>Muscle Maintenance,</li>
          <li>Skin and Coat Health.</li>
        </ul>
      </div>
      <div class="allergy">
        <svg width="20" height="20" viewBox="0 0 20 20" aria-hidden="true">
          <circle cx="10" cy="10" r="9" fill="var(--leaf)"/>
          <path d="M6 10.5l3 3 5-6" fill="none" stroke="#fff" stroke-width="1.8" stroke-linecap="round"/>
        </svg>
        Allergy-Friendly
      </div>
    </section>

    <section class="panel panel--info">
      <div class="about">Quillory's mealworm supplement is crafted to give your pet a nutritious boost. Rich in protein, mealworms support muscle maintenance and help your pet have a glossy, healthy coat. Quillory's blend is the perfect addition to daily nutrition and wellbeing.</div>
      <div class="ingredients">
        <span class="tag">INGREDIENTS</span>
        <p>Mealworms, Sweet potato, Oats, Dried carrots, Rosemary extract (a natural preservative), Vitamin and mineral blend.</p>
      </div>
      <div class="contact">
        <strong>For Inquiries:</strong><br>
        Phone: 555-0142<br>
        Email: hello@quillory.example<br>
        Website: www.quillory.example
      </div>
      <div class="batch">Batch No: QL-2407<br>Expiry: 07/2026</div>
      <div class="edge-strip" aria-hidden="true"></div>
    </section>

    <footer class="bottom-band">QUALITY GUARANTEED. SATISFACTION ASSURED.</footer>
  </main>
</body>
</html>
```